Business Card Design Project

Card should be standard size
Logo placed in upper right corner and slogan upper left corner
English Name of company in middle under that Chinese name
Office address across bottom of card including phone number
My Name and title

Target Market(s)

Start-ups and small to medium size businesses
age 30-55

Industry/Entity Type

Business

Font styles to use
Sans Serif

Colors
ffffff

```html
<!DOCTYPE html>
<html lang="en">
<head>
<meta charset="utf-8">
<title>Meridian Business Card</title>
<link href="https://fonts.googleapis.com/css2?family=Lato:ital,wght@0,400;0,700;1,400&family=Noto+Sans+SC:wght@400;500&display=swap" rel="stylesheet">
<style>
  :root {
    --stage: #000000;
    --card: #f3f3f4;
    --ink: #0f3e6b;
    --ink-soft: #163a63;
  }
  html, body {
    margin: 0;
    padding: 0;
    width: 1200px;
    height: 1000px;
    overflow: hidden;
    background: var(--stage);
  }
  .card {
    position: absolute;
    left: 150px;
    top: 250px;
    width: 900px;
    height: 500px;
    background: var(--card);
    font-family: "Lato", sans-serif;
    color: var(--ink);
  }
  .slogan {
    position: absolute;
    left: 0;
    top: 28px;
    width: 250px;
    text-align: center;
    font-weight: 700;
    font-size: 17px;
    line-height: 22px;
    color: var(--ink-soft);
    margin: 0;
  }
  .brand {
    position: absolute;
    left: 700px;
    top: 200px;
    width: 182px;
    margin: 0;
    text-align: center;
    font-weight: 700;
    font-size: 30px;
    line-height: 36px;
    color: var(--ink);
  }
  .center {
    position: absolute;
    left: 0;
    width: 900px;
    text-align: center;
    margin: 0;
  }
  .person-name { top: 146px; font-weight: 700; font-size: 48px; line-height: 54px; letter-spacing: 0.5px; }
  .person-title { top: 195px; font-style: italic; font-size: 34px; line-height: 40px; }
  .person-email { top: 232px; font-size: 19px; line-height: 24px; }
  .company-cn {
    top: 303px;
    font-family: "Noto Sans SC", sans-serif;
    font-weight: 500;
    font-size: 24px;
    line-height: 34px;
    letter-spacing: 1px;
  }
  .company-en { top: 338px; font-size: 20px; line-height: 26px; }
  .address { top: 392px; font-size: 20px; line-height: 26px; }
  .phone { top: 420px; font-size: 20px; line-height: 26px; }
  .website { top: 452px; font-weight: 700; font-size: 17px; line-height: 22px; }
</style>
</head>
<body>
  <div class="card">
    <p class="slogan">Your Goal is Ours,<br>Let's get there together</p>

    <p class="brand">Meridian</p>

    <h1 class="center person-name">Daniel Hart</h1>
    <p class="center person-title">President &amp; CEO</p>
    <p class="center person-email">daniel.hart@meridianchina.com</p>

    <p class="center company-cn" lang="zh">恒远商务信息咨询（上海）有限公司</p>
    <p class="center company-en">Meridian Assets And Property Management<br>Consulting (Shanghai) Co., Ltd.</p>
    <p class="center address">Lin Feng Road 288, suite 510-512, Baoshan Dist., Shanghai</p>
    <p class="center phone">Phone: 86-13755508124</p>
    <p class="center website">www.meridianchina.com</p>
  </div>
</body>
</html>
```